Marriage Retreat: 4 Page Color Brochure

I need a 4 page, full color brochure that is 8.5 x 11 when folded (11 x 17 front/back when printed/unfolded). The brochure is to inform pastors and religious leaders about a private retreat to help them strengthen their marriages. Attached you will find: (1) a Word document with the copy/text and initial guidelines on the page layout (although some flexibility on what text goes on which page is acceptable); (2) a creative brief PDF with some of the visual ideas I have to jumpstart your thinking; (3) logo files for the organization Brightwater Circle (the logo must be included); (4) original scan of tree artwork that can be used as a visual element (this is the same tree that has been converted to a vector file in the logo; please use a color scheme in the brochure that is complementary to this artwork). The overall feel for this piece should be timeless, classic, welcoming and approachable. The font in the logo is Audrey, although it has been stylized a bit. Please take that into account when selecting fonts for the layout. I do not yet have the photo of Tom & Norma (the hosts of this retreat) for you to include with their bios. Please insert a placeholder image for now and I will get you the actual photo in a few days. Once we get to the final stage, I would also like to have a version of the file that is laid out as 4 individual 8.5x11 pages so it can be printed in that format if needed. I would also like to have a PDF version of each file.

Target Market(s)

The initial target market for this type of service will be males (who typically recommend the service to couples), but the ultimate decision maker will probably be a female (the wife of the couple that will attend the retreat).

Industry/Entity Type

Counseling

Font styles to use
Serif
Sans Serif
Other font styles liked:
• Audrey

Colors

Designer to choose colors to be used in the design.

Requirements
Must have
• Logo for Brightwater Circle. Color scheme that is complementary to the tree artwork provided. Font that incorporates or complements the font in the logo - Audrey. Photo of Tom & Norma with their bio (use a placeholder for now). Please include at least one or two stock photos of married couples somewhere in the brochure. See the examples in the creative brief and please let me know if you need me to provide the actual files (if you do not have access to Kelvora Images).
Nice to have
• A design option that includes an infographic/icon style for me to consider. See creative brief document for more on this idea.
Should not have
• Note: I removed the prior instructions indicating this design should not have a full page bleed. That is no longer a limitation on this design. Feel free to go with what you think looks best to make your submission as strong as possible.

```html
<!DOCTYPE html>
<html lang="en">
<head>
<meta charset="utf-8">
<title>Brightwater Circle – Retreat Brochure</title>
<link href="https://fonts.googleapis.com/css2?family=Libre+Baskerville&family=Nunito+Sans:ital,wght@0,400;0,700;1,400&display=swap" rel="stylesheet">
<style>
:root{
  --canvas:#d9dadc;
  --paper:#ffffff;
  --green-deep:#4c7844;
  --green-head:#3f6b38;
  --green-pill:#3d6e35;
  --olive-light:#a6b670;
  --olive-dark:#5f5a2c;
  --brown-line:#6a5a2e;
  --ink:#4a4a4a;
  --ink-soft:#5c5c5c;
  --serif:"Libre Baskerville", Georgia, serif;
  --sans:"Nunito Sans", Arial, sans-serif;
}
*{box-sizing:border-box;margin:0;padding:0}
h1,h2{font-weight:400}
html,body{width:920px;height:1200px;overflow:hidden;background:var(--canvas)}
.canvas{position:relative;width:920px;height:1200px;font-family:var(--sans);color:var(--ink)}
.spread{position:absolute;left:57px;width:828px;height:536px;display:flex;box-shadow:0 10px 14px -6px rgba(0,0,0,.35)}
.spread--outer{top:29px}
.spread--inner{top:618px}
.page{position:relative;width:414px;height:536px;background:var(--paper);overflow:hidden}
.page--left::after{content:"";position:absolute;top:0;right:0;width:40px;height:100%;background:linear-gradient(to right,rgba(0,0,0,0),rgba(0,0,0,.07));pointer-events:none}
.page--right::after{content:"";position:absolute;top:0;left:0;width:30px;height:100%;background:linear-gradient(to left,rgba(0,0,0,0),rgba(0,0,0,.06));pointer-events:none}
.shape{position:absolute;left:0;top:0;width:414px;height:536px}

/* agenda */
.agenda{position:absolute;left:0;top:0;width:414px;height:181px;background:var(--olive-light)}
.agenda__title{position:absolute;top:10px;width:100%;text-align:center;font-family:var(--serif);font-size:15px;color:#fff;letter-spacing:.3px}
.agenda__day{position:absolute;top:35px;width:126px}
.agenda__pill{width:110px;height:12px;border-radius:6px;background:#fff;box-shadow:1px 1px 2px rgba(0,0,0,.25);font-size:7px;line-height:12px;text-align:center;color:#333}
.agenda__list{list-style:none;margin-top:10px;color:#fff;font-size:6.7px;line-height:9.45px}
.agenda__list li{position:relative;padding-left:7px;white-space:nowrap}
.agenda__list li::before{content:"";position:absolute;left:0;top:3px;width:4px;height:4px;border-radius:50%;background:#fff}
.agenda__note{position:absolute;top:167px;width:100%;text-align:center;font-size:5.6px;color:#fff}

.heading-cta{position:absolute;left:16px;top:240px;font-family:var(--serif);font-size:16px;color:var(--green-head);white-space:nowrap}
.brand{position:absolute;text-align:center;font-family:var(--serif);color:var(--olive-dark)}
.brand__dot{display:block;margin:0 auto 6px;border-radius:50%;background:var(--olive-light)}
.contact{position:absolute;left:144px;top:297px;width:256px;font-size:8.4px;line-height:12.8px;color:var(--ink);text-align:justify}
.contact p+p{margin-top:13px}
.contact strong{font-weight:700;color:#333}
.credits{position:absolute;left:0;top:466px;width:414px;text-align:center;font-size:5.6px;line-height:9.5px;color:#fff}

.cover-title{position:absolute;top:456px;width:100%;text-align:center;font-family:var(--serif);font-size:25px;color:#fff;letter-spacing:.5px;white-space:nowrap}
.cover-sub{position:absolute;top:499px;width:100%;text-align:center;font-size:12.5px;color:#fff}

/* inner left */
.risk__title{position:absolute;left:16px;top:130px;font-family:var(--serif);font-size:12px;color:var(--olive-dark);white-space:nowrap}
.stat{position:absolute;left:16px;width:398px;height:12px}
.stat__strip{position:absolute;left:140px;right:0;top:1px;height:11px;background:rgba(255,255,255,.9)}
.stat__bar{position:absolute;left:0;top:0;width:145px;height:12px;border-radius:6px;background:var(--olive-light);overflow:hidden}
.stat__fill{height:100%;background:var(--green-head);border-radius:6px 0 0 6px}
.stat__num{position:absolute;left:6px;top:0;font-family:var(--serif);font-size:7.5px;line-height:12px;color:#fff}
.stat__text{position:absolute;left:156px;top:0;font-size:6.6px;line-height:12px;color:#333;white-space:nowrap}
.section-title{position:absolute;width:100%;text-align:center;font-family:var(--serif);font-size:12px;color:var(--olive-dark);white-space:nowrap}
.quote{position:absolute;width:187px;border:1px solid var(--brown-line);border-radius:4px;padding:9px 5px 4px;font-style:italic;font-size:6px;line-height:8.1px;color:var(--ink-soft);text-align:justify}
.quote__mark{position:absolute;top:-12px;left:50%;transform:translateX(-50%);background:#fff;padding:0 3px;font-family:var(--serif);font-style:normal;font-size:26px;line-height:22px;height:16px;overflow:hidden;color:var(--olive-dark)}
.footer-band{position:absolute;left:0;bottom:0;width:414px;height:11px;background:var(--olive-light)}

/* inner right */
.hosts__photo{position:absolute;left:12px;top:219px;width:53px;height:66px}
.body-copy{font-size:7.2px;line-height:10.8px;color:var(--ink)}
.hosts__bio{position:absolute;left:75px;top:219px;width:330px;text-align:justify}
.hosts__bio strong{color:#333}
.center-copy{position:absolute;left:10px;width:394px;text-align:center}
.goal{position:absolute;top:397px;width:109px;height:62px;border:1px solid var(--brown-line);border-radius:5px;background:#fff}
.goal__head{height:16px;margin:-1px -1px 0;border-radius:5px 5px 0 0;background:var(--green-pill);color:#fff;font-size:7px;line-height:16px;text-align:center;box-shadow:0 2px 3px rgba(0,0,0,.25)}
.goal__text{padding:8px 6px 0;text-align:center;font-size:7.2px;line-height:10.5px;color:var(--ink)}
</style>
</head>
<body>
<div class="canvas">

  <section class="spread spread--outer">
    <article class="page page--left">
      <div class="agenda">
        <h2 class="agenda__title">SAMPLE AGENDA</h2>
        <div class="agenda__day" style="left:16px">
          <div class="agenda__pill">Day One</div>
          <ul class="agenda__list">
            <li>Arrive, settle in, get acquainted</li>
            <li>Individual reflection and</li>
            <li style="padding-left:7px" class="cont">couple connection</li>
            <li>Lunch</li>
            <li>Session 1*</li>
            <li>Break</li>
            <li>Session 2</li>
            <li>Free time</li>
            <li>Dinner</li>
            <li>5 minute huddle</li>
          </ul>
        </div>
        <div class="agenda__day" style="left:148px">
          <div class="agenda__pill">Day Two</div>
          <ul class="agenda__list">
            <li>Coffee, individual reflection,</li>
            <li class="cont">time with God</li>
            <li>Breakfast</li>
            <li>Couple breakout</li>
            <li>Session 3</li>
            <li>Break</li>
            <li>Lunch</li>
            <li>Sessions 4 &amp; 5: Building Bridges</li>
            <li>Dinner date (couple only)</li>
            <li>5 minute huddle</li>
          </ul>
        </div>
        <div class="agenda__day" style="left:281px">
          <div class="agenda__pill">Day Three</div>
          <ul class="agenda__list">
            <li>Coffee, individual reflection</li>
            <li class="cont">and time with God</li>
            <li>Breakfast</li>
            <li>Session 6: Integrated Intimacy</li>
            <li>Lunch</li>
            <li>Break</li>
            <li>Session 7</li>
            <li>Wrap up, next steps</li>
            <li>Pray</li>
            <li>Depart</li>
          </ul>
        </div>
        <p class="agenda__note">* Each session lasts approximately 2 hours and includes time with the hosts and breakouts for reflection and exercises.</p>
      </div>
      <style>.agenda__list li.cont::before{display:none}</style>

      <h2 class="heading-cta">READY TO INVEST IN YOUR MARRIAGE?</h2>

      <div class="brand" style="left:14px;top:300px;width:112px">
        <span class="brand__dot" style="width:46px;height:46px"></span>
        <span style="font-size:11px">Brightwater Circle</span>
      </div>

      <div class="contact">
        <p>Contact Tom &amp; Norma Hale to request a confidential initial consultation: <strong>info@brightwatercircle.org</strong></p>
        <p>Retreat expenses are covered for you – including meals, lodging, teaching and materials. Couples are responsible for their own transportation to the retreat and childcare, if needed. Additional scholarships are available.</p>
      </div>

      <svg class="shape" viewBox="0 0 414 536" aria-hidden="true">
        <path d="M0,478 Q200,442 414,434" fill="none" stroke="var(--brown-line)" stroke-width="3"/>
        <path d="M0,484 Q200,448 414,440 L414,536 L0,536 Z" fill="var(--green-deep)"/>
      </svg>
      <div class="credits">
        <p>¹The Corbin Institute, 2006</p>
        <p>²The Halden Research Group, Ministry Life Survey, 2017</p>
        <p>Testimonials have been edited for clarity and confidentiality.</p>
        <p>Tree artwork by Mara Ellison. Photo of Hales by Reed Calloway Photography</p>
        <p>©Tom and Norma Hale.</p>
      </div>
    </article>

    <article class="page page--right">
      <div class="brand" style="left:107px;top:30px;width:200px">
        <span class="brand__dot" style="width:60px;height:60px"></span>
        <span style="font-size:15px">Brightwater Circle</span>
      </div>

      <svg class="shape" viewBox="0 0 414 536" role="img" aria-label="Photo: a couple holding hands in a sunny green meadow">
        <defs>
          <linearGradient id="meadow" x1="0" y1="0" x2="0" y2="1">
            <stop offset="0" stop-color="#d8dcc9"/>
            <stop offset=".35" stop-color="#a9a17f"/>
            <stop offset=".7" stop-color="#7f9a4a"/>
            <stop offset="1" stop-color="#5f8030"/>
          </linearGradient>
        </defs>
        <path d="M0,140 Q170,172 414,176 L414,440 Q200,430 0,436 Z" fill="url(#meadow)"/>
      </svg>
      <svg class="shape" viewBox="0 0 414 536" aria-hidden="true">
        <path d="M0,108 Q160,160 414,168 L414,176 Q170,172 0,140 Z" fill="var(--olive-light)"/>
        <path d="M0,432 Q220,424 414,438" fill="none" stroke="var(--brown-line)" stroke-width="3"/>
        <path d="M0,438 Q220,430 414,444 L414,536 L0,536 Z" fill="var(--green-deep)"/>
      </svg>
      <h1 class="cover-title">BRIGHTWATER CIRCLE</h1>
      <p class="cover-sub">A Personalized Retreat for Couples in Ministry</p>
    </article>
  </section>

  <section class="spread spread--inner">
    <article class="page page--left">
      <svg class="shape" viewBox="0 0 414 536" role="img" aria-label="Photo: a couple in conversation at home">
        <defs>
          <linearGradient id="room" x1="0" y1="0" x2="1" y2="0">
            <stop offset="0" stop-color="#eeece8"/>
            <stop offset=".5" stop-color="#c9cfd6"/>
            <stop offset="1" stop-color="#e6e1d8"/>
          </linearGradient>
        </defs>
        <path d="M0,0 H414 V196 Q250,232 0,206 Z" fill="url(#room)"/>
      </svg>
      <svg class="shape" viewBox="0 0 414 536" aria-hidden="true">
        <path d="M0,200 Q250,226 414,194 L414,202 Q250,238 0,212 Z" fill="var(--olive-light)"/>
        <path d="M0,212 Q250,238 414,202" fill="none" stroke="var(--brown-line)" stroke-width="2.5"/>
      </svg>

      <h2 class="risk__title">MINISTRY MARRIAGES ARE AT RISK</h2>
      <div class="stat" style="top:155px">
        <div class="stat__strip"></div>
        <div class="stat__bar"><div class="stat__fill" style="width:77%"></div></div>
        <span class="stat__num">77%</span>
        <span class="stat__text">of pastors feel they do not have a good marriage¹</span>
      </div>
      <div class="stat" style="top:171px">
        <div class="stat__strip"></div>
        <div class="stat__bar"><div class="stat__fill" style="width:48%"></div></div>
        <span class="stat__num">48%</span>
        <span class="stat__text">say their current ministry role has been difficult on their marriage²</span>
      </div>
      <div class="stat" style="top:187px">
        <div class="stat__strip"></div>
        <div class="stat__bar"><div class="stat__fill" style="width:26%"></div></div>
        <span class="stat__num">26%</span>
        <span class="stat__text">of pastors face significant marital problems²</span>
      </div>

      <h2 class="section-title" style="top:263px">EXPERIENCE TRANSFORMATION</h2>

      <blockquote class="quote" style="left:14px;top:303px;height:57px"><span class="quote__mark">“</span>Our marriage was in crisis. The stress of ministry had taken a deep toll on us and in the worst moments we didn't even like each other anymore. Tom and Norma are people we trust with the darkest moments of our lives. They stood with us and held up our arms to allow us to continue.</blockquote>
      <blockquote class="quote" style="left:213px;top:303px;height:57px"><span class="quote__mark">“</span>Tom and Norma meet people in their pain and brokenness without shame or judgment and gently help them make major shifts from a place of extreme distress to a hopeful and productive path forward.</blockquote>
      <blockquote class="quote" style="left:14px;top:372px;height:58px"><span class="quote__mark">“</span>During a critical time, Tom and Norma helped us navigate our marriage around the traps that we so easily and repeatedly fell into... We were sitting ducks for the evil one... They took us to the deep end of the marriage pool and dove in first. I see a more fruitful and God honoring marriage ahead.</blockquote>
      <blockquote class="quote" style="left:213px;top:372px;height:58px"><span class="quote__mark">“</span>Tom and Norma understand the sanctity of safely and compassionately learning from each other's stories...the triumphs, the failures, the times of healing, and the times of deep woundedness. They hold the stories of the couples they work tenderly, confidentially and dearly.</blockquote>
      <blockquote class="quote" style="left:14px;top:442px;height:56px"><span class="quote__mark">“</span>This experience was the most important thing I have ever done in my life outside of saying yes to Jesus. As a pastor, I have always known that my family is my number one ministry. This experience helped me take that theoretical goal and turn it into a reality.</blockquote>
      <blockquote class="quote" style="left:213px;top:442px;height:56px"><span class="quote__mark">“</span>Tom and Norma exemplify these qualities: a safety zone with in-the-vault assurance, advice grounded in scripture, a straightforward message, truth spoken in love even when painful, vulnerability and authenticity.</blockquote>

      <div class="footer-band"></div>
    </article>

    <article class="page page--right">
      <svg class="shape" viewBox="0 0 414 536" role="img" aria-label="Photo: a smiling couple reading books together on a grassy lawn">
        <defs>
          <linearGradient id="lawn" x1="0" y1="0" x2="0" y2="1">
            <stop offset="0" stop-color="#b7c66a"/>
            <stop offset=".45" stop-color="#7f9a3a"/>
            <stop offset="1" stop-color="#5d7f2a"/>
          </linearGradient>
        </defs>
        <path d="M0,0 H414 V186 Q260,160 0,190 Z" fill="url(#lawn)"/>
      </svg>
      <svg class="shape" viewBox="0 0 414 536" aria-hidden="true">
        <path d="M0,186 Q260,156 414,182 L414,194 Q260,166 0,196 Z" fill="var(--olive-light)"/>
        <path d="M0,196 Q260,166 414,194" fill="none" stroke="var(--brown-line)" stroke-width="2"/>
      </svg>

      <h2 class="section-title" style="top:198px">YOUR HOSTS</h2>
      <svg class="hosts__photo" viewBox="0 0 53 66" role="img" aria-label="Photo placeholder: portrait of hosts Tom and Norma Hale">
        <rect width="53" height="66" fill="#8d8478"/>
        <rect width="53" height="66" fill="#5a524b" opacity=".35"/>
      </svg>
      <p class="hosts__bio body-copy"><strong>Tom and Norma Hale</strong> bring more than 20 years of experience helping build and restore Christ-centered marriages. They have experienced God's redemption in their own broken stories. A compassionate and insightful listener, Tom is a retired energy industry leader currently serving on a corporate board and church overseer board. Norma formerly served in full-time ministry and is a gifted teacher who delights in unpacking God's truth. God has used the time and tools they offer to transform many marriages.</p>

      <h2 class="section-title" style="top:305px">A RETREAT FOR COUPLES IN MINISTRY</h2>
      <p class="center-copy body-copy" style="top:324px">Brightwater Circle retreats provide you time, space, and Bible-based tools to cultivate a life-giving marriage.</p>

      <h2 class="section-title" style="top:346px">YOUR INVITATION</h2>
      <p class="center-copy body-copy" style="top:366px;left:55px;width:304px">Whether your marriage is thriving, in distress, or needs a fresh start, Brightwater Circle retreats equip couples in ministry to:</p>

      <div class="goal" style="left:19px"><div class="goal__head">Deepen Intimacy</div><p class="goal__text">Reinvigorate love by being heard and valued</p></div>
      <div class="goal" style="left:151px"><div class="goal__head">Untangle Relational Knots</div><p class="goal__text">Heal hurts, care for yourself and each other with grace</p></div>
      <div class="goal" style="left:283px"><div class="goal__head">Replenish Joy</div><p class="goal__text">Create an environment to grow and rediscover fun</p></div>

      <p class="center-copy body-copy" style="top:476px">The 3-day retreat is personally tailored for one couple only. We provide a lovely, comfortable, private and safe setting where everything is taken care of. We can welcome you to our locations in Austin and Chicago or – in special circumstances – bring the retreat to your area.</p>

      <div class="footer-band"></div>
    </article>
  </section>
</div>
</body>
</html>
```